CV Template

We need a graphic design to our new CV templates for our consultants. We are a small young Danish upcoming IT-business company making software solutions for our customers etc. You can visit our new website here: dev.lunavaerket.com, then you can see our web design, colors etc. I have attached a file for your inspiration :-) In the presentation I would like to have a picture of the employee, some text who descripe the profile/consultant and then I imagine that there is a table where we can write the employee's skills etc.

I would like the design to be "fresh & catchy" :-)

Looking forward to hear from you.

Best regards,
Sanne

```html
<!DOCTYPE html>
<html lang="da">
<head>
<meta charset="utf-8">
<title>Lunaværket – CV</title>
<link href="https://fonts.googleapis.com/css2?family=Encode+Sans+Semi+Condensed:wght@300;400;600;700&display=swap" rel="stylesheet">
<style>
  :root{
    --navy:#234e6a;
    --ink:#2b2b2b;
    --accent:#c9561a;
    --rule:#c9d3da;
    --gap:#c8c8c8;
    --paper:#ffffff;
    --photo-a:#d9d6d0;
    --photo-b:#9a8f83;
  }
  *{box-sizing:border-box;margin:0;padding:0}
  html,body{width:1200px;height:755px;overflow:hidden;background:var(--gap)}
  body{font-family:"Encode Sans Semi Condensed",sans-serif;color:var(--ink);position:relative}
  .page{position:absolute;top:0;height:755px;background:var(--paper);overflow:hidden}
  .page--front{left:0;width:595px;border-left:1px solid #bbb}
  .page--back{left:608px;width:592px}
  .side-band{position:absolute;top:0;right:0;width:95px;height:755px;background:var(--navy)}
  .abs{position:absolute}

  .brand{left:49px;top:36px;display:flex;align-items:center;gap:7px}
  .brand__mark{width:8px;height:8px;background:var(--navy);border-radius:50%}
  .brand__name{font-size:22px;font-weight:300;letter-spacing:1px;color:var(--navy);line-height:1}

  .portrait{left:48px;top:86px;width:148px;height:114px;border:1px solid var(--navy);padding:3px;background:var(--paper)}
  .portrait__fill{width:100%;height:100%;background:radial-gradient(ellipse at 50% 45%,var(--photo-b),var(--photo-a) 70%)}

  .profile{left:216px;top:86px;width:246px}
  .profile__name{font-size:21px;font-weight:400;color:var(--navy);letter-spacing:-.6px;text-transform:uppercase;line-height:26px}
  .profile__bio{margin-top:7px;font-size:10px;font-weight:300;color:var(--navy);line-height:21.3px;text-align:justify;letter-spacing:-.1px}

  .section{width:413px}
  .section__title{font-size:11.5px;font-weight:600;color:var(--navy);display:inline-block;border-bottom:1.5px solid var(--navy);padding-bottom:3px;line-height:13px}
  .section__rule{border-top:1px solid var(--rule);margin-top:-1px}
  .section__text{margin-top:7px;font-size:10px;font-weight:300;line-height:21.3px;text-align:justify;letter-spacing:-.1px}

  .skills{border-collapse:collapse;margin-top:8px;font-size:10px;font-weight:300}
  .skills th{color:var(--accent);font-weight:600;text-align:left;font-size:9px;height:20px;letter-spacing:-.4px}
  .skills td{height:29px}
  .skills .c1{width:91px}.skills .c2{width:175px}
  .stars{display:flex;gap:9px}
  .stars svg{width:15px;height:15px;fill:var(--navy)}

  .contact{transform:rotate(-90deg);transform-origin:0 0;color:#fff;white-space:nowrap}
  .contact__name{font-size:15px;font-weight:700;line-height:19px}
  .contact__address{font-size:10.5px;font-weight:400;line-height:16px}
  .contact__lines{display:flex;align-items:center;gap:18px;font-size:8.5px;font-style:italic;line-height:15px}
  .contact__item{display:flex;align-items:center;gap:6px}
  .contact__item svg{width:10px;height:10px;fill:#fff}
</style>
</head>
<body>
<svg width="0" height="0" style="position:absolute">
  <symbol id="star" viewBox="0 0 24 24"><path d="M12 1.5l3.1 7 7.4.6-5.6 4.9 1.7 7.4L12 17.5 5.4 21.4l1.7-7.4L1.5 9.1l7.4-.6z"/></symbol>
  <symbol id="phone" viewBox="0 0 24 24"><path d="M6.6 10.8a15 15 0 006.6 6.6l2.2-2.2c.3-.3.7-.4 1-.2 1.1.4 2.3.6 3.6.6.6 0 1 .4 1 1V20c0 .6-.4 1-1 1A17 17 0 013 4c0-.6.4-1 1-1h3.5c.6 0 1 .4 1 1 0 1.2.2 2.4.6 3.6.1.3 0 .7-.2 1z"/></symbol>
  <symbol id="mail" viewBox="0 0 24 24"><path d="M2 5h20v14H2zm2 2v.5l8 5 8-5V7zm0 3v7h16v-7l-8 5z"/></symbol>
</svg>

<section class="page page--front">
  <div class="abs brand">
    <span class="brand__mark"></span><span class="brand__name">LUNAVÆRKET</span>
  </div>

  <div class="abs portrait"><div class="portrait__fill" role="img" aria-label="Portrait photo of the consultant"></div></div>

  <div class="abs profile">
    <h1 class="profile__name">Mikkel Test</h1>
    <p class="profile__bio">Here could be a very brief description of the particular employee. Possibly some sort of biography or other type of information. It would be best if this text box would end right here so it aligns with the bottom of the picture.</p>
  </div>

  <div class="abs section" style="left:50px;top:223px">
    <h2 class="section__title">Category</h2><div class="section__rule"></div>
    <p class="section__text">Here is your text for the specific category. Here is your text for the specific category. Here is your text for the specific category. Here is your text for the specific category. Here is your text for the specific category. Here is your text for the specific category. Here is your text for the specific category. Here is your text for the specific category.</p>
  </div>

  <div class="abs section" style="left:50px;top:348px">
    <h2 class="section__title">Skills</h2><div class="section__rule"></div>
    <table class="skills">
      <thead><tr><th class="c1">SKILL:</th><th class="c2">CATEGORY:</th><th>LEVEL:</th></tr></thead>
      <tbody>
        <tr><td>Skill 1</td><td>Some Sort of Text</td><td><div class="stars"><svg><use href="#star"/></svg><svg><use href="#star"/></svg><svg><use href="#star"/></svg></div></td></tr>
        <tr><td>Skill 2</td><td>Some Sort of Text</td><td><div class="stars"><svg><use href="#star"/></svg><svg><use href="#star"/></svg><svg><use href="#star"/></svg></div></td></tr>
        <tr><td>Skill 3</td><td>Some Sort of Text</td><td><div class="stars"><svg><use href="#star"/></svg><svg><use href="#star"/></svg><svg><use href="#star"/></svg></div></td></tr>
        <tr><td>Skill 4</td><td>Some Sort of Text</td><td><div class="stars"><svg><use href="#star"/></svg></div></td></tr>
        <tr><td>Skill 5</td><td>Some Sort of Text</td><td><div class="stars"><svg><use href="#star"/></svg><svg><use href="#star"/></svg></div></td></tr>
      </tbody>
    </table>
  </div>

  <div class="abs section" style="left:50px;top:556px">
    <h2 class="section__title">Category</h2><div class="section__rule"></div>
    <p class="section__text">Here is your text for the specific category. Here is your text for the specific category. Here is your text for the specific category. Here is your text for the specific category. Here is your text for the specific category. Here is your text for the specific category. Here is your text for the specific category. Here is your text for the specific category.</p>
  </div>

  <aside class="side-band">
    <div class="abs contact" style="left:23px;top:712px">
      <div class="contact__name">LUNAVÆRKET</div>
      <div class="contact__address">Solsortevej 12 - 2100 København Ø - Denmark</div>
      <div class="contact__lines">
        <span class="contact__item"><svg><use href="#mail"/></svg>info@lunavaerket.dk</span>
        <span class="contact__item"><svg><use href="#phone"/></svg>+45 70 20 30 40</span>
      </div>
    </div>
  </aside>
</section>

<section class="page page--back">
  <div class="abs section" style="left:48px;top:24px">
    <h2 class="section__title">Category</h2><div class="section__rule"></div>
    <p class="section__text">Here is your text for the specific category. Here is your text for the specific category. Here is your text for the specific category. Here is your text for the specific category. Here is your text for the specific category. Here is your text for the specific category. Here is your text for the specific category. Here is your text for the specific category.</p>
  </div>
  <div class="abs section" style="left:48px;top:150px">
    <h2 class="section__title">Category</h2><div class="section__rule"></div>
    <p class="section__text">Here is your text for the specific category. Here is your text for the specific category. Here is your text for the specific category. Here is your text for the specific category. Here is your text for the specific category. Here is your text for the specific category. Here is your text for the specific category. Here is your text for the specific category.</p>
  </div>
  <div class="abs section" style="left:48px;top:275px">
    <h2 class="section__title">Category</h2><div class="section__rule"></div>
    <p class="section__text">Here is your text for the specific category. Here is your text for the specific category. Here is your text for the specific category. Here is your text for the specific category. Here is your text for the specific category. Here is your text for the specific category. Here is your text for the specific category. Here is your text for the specific category.</p>
  </div>

  <aside class="side-band">
    <div class="abs contact" style="left:23px;top:712px">
      <div class="contact__name">LUNAVÆRKET</div>
      <div class="contact__address">Solsortevej 12 - 2100 København Ø - Denmark</div>
      <div class="contact__lines">
        <span class="contact__item"><svg><use href="#mail"/></svg>info@lunavaerket.dk</span>
        <span class="contact__item"><svg><use href="#phone"/></svg>+45 70 20 30 40</span>
      </div>
    </div>
  </aside>
</section>
</body>
</html>
```